Business Card Design for an Investment Company

We need a business card design for our private investment company, called Ashbourne Partners. Ashbourne Partners is an investments partnership that aims to acquire shares in listed companies with a view to influencing those companies through active dialogue in order to improve their value. We need designs that use the logo colors (blue, grey, white), we need both English and Arabic on the business cards (can be on one side or 2 sides). The final logo should communicate professionalism, conservatism (nothing too fancy or too cheesy), that we are smart, conservative and old school.

Target Market(s)

Investment companies

Industry/Entity Type

Investment

Contact Information for Business Card

Khalid Yousef Rumaithi
Senior Executive Officer

Palm Terrace 07, Level 3, Office 215/12
HLMZ

+9714987650
krumaithi@ashbournepartners.com
www.ashbournepartners.com

Requirements
Must have
• Logo to be placed on the left hand side of the business card
• for the Arabic, we only need to have the name and title so it can be accomodated on one side so we can have the other side with full color and logo. The arabic that needs to be used is the below:
• خالد يوسف الرميثي
• المدير التنفيدي

```html
<!DOCTYPE html>
<html lang="en">
<head>
<meta charset="utf-8">
<title>Ashbourne Partners — Business Card</title>
<link rel="stylesheet" href="https://fonts.googleapis.com/css2?family=Montserrat:wght@500;700;800&family=Roboto:wght@400;500&family=Noto+Naskh+Arabic:wght@500;700&display=swap">
<style>
  :root {
    --brand-blue: #1d70a8;
    --brand-grey: #5b5b5d;
    --card-white: #ffffff;
    --hairline: #d6d6d8;
    --hatch: #f1f1f3;
    --text-dark: #3a3a3c;
    --stage: #6b6b6e;
  }
  * { margin: 0; padding: 0; box-sizing: border-box; }
  html, body { width: 1200px; height: 749px; overflow: hidden; }
  body {
    background: var(--stage);
    display: flex;
    align-items: center;
    justify-content: center;
    gap: 60px;
  }
  .card {
    width: 500px;
    height: 290px;
    display: block;
    border-radius: 24px;
    box-shadow: 0 14px 30px rgba(0,0,0,.28);
  }
  .brand-name { font-family: "Montserrat", sans-serif; font-weight: 800; fill: var(--brand-blue); }
  .web-line { font-family: "Roboto", sans-serif; font-weight: 500; fill: var(--card-white); }
  .person-first { font-family: "Montserrat", sans-serif; font-weight: 800; fill: var(--brand-blue); }
  .person-last { font-family: "Montserrat", sans-serif; font-weight: 800; fill: var(--brand-grey); }
  .person-role { font-family: "Montserrat", sans-serif; font-weight: 500; fill: var(--text-dark); letter-spacing: 1.5px; }
  .person-name-ar { font-family: "Noto Naskh Arabic", serif; font-weight: 700; fill: var(--brand-blue); }
  .person-role-ar { font-family: "Noto Naskh Arabic", serif; font-weight: 500; fill: var(--text-dark); }
  .contact-line { font-family: "Roboto", sans-serif; font-weight: 400; fill: var(--text-dark); }
</style>
</head>
<body>

  <!-- Front side -->
  <svg class="card card-front" viewBox="0 0 500 290" aria-label="Ashbourne Partners business card, front">
    <defs><clipPath id="front-shape"><rect width="500" height="290" rx="24"/></clipPath></defs>
    <g clip-path="url(#front-shape)">
      <rect class="card-base" width="500" height="290" fill="var(--card-white)"/>
      <g class="accent-stripes accent-right" stroke="var(--brand-blue)" stroke-width="2.5">
        <line x1="400" y1="150" x2="500" y2="150"/>
        <line x1="410" y1="159" x2="500" y2="159"/>
        <line x1="420" y1="168" x2="500" y2="168"/>
      </g>
      <rect class="web-band" x="0" y="178" width="500" height="40" fill="var(--brand-blue)"/>
      <g class="accent-stripes accent-left" stroke="var(--brand-blue)" stroke-width="2.5">
        <line x1="0" y1="228" x2="100" y2="228"/>
        <line x1="0" y1="237" x2="90" y2="237"/>
        <line x1="0" y1="246" x2="80" y2="246"/>
      </g>
      <rect class="brand-mark" x="48" y="97" width="26" height="26" fill="var(--brand-grey)"/>
      <text class="brand-name" x="84" y="121" font-size="30">Ashbourne Partners</text>
      <circle cx="190" cy="198" r="3.5" fill="none" stroke="var(--card-white)" stroke-width="1.3"/>
      <text class="web-line" x="200" y="202" font-size="11">www.ashbournepartners.com</text>
    </g>
  </svg>

  <!-- Back side -->
  <svg class="card card-back" viewBox="0 0 500 290" aria-label="Ashbourne Partners business card, back">
    <defs><clipPath id="back-shape"><rect width="500" height="290" rx="24"/></clipPath></defs>
    <g clip-path="url(#back-shape)">
      <rect class="card-base" width="500" height="290" fill="var(--card-white)"/>
      <rect class="top-tint" width="500" height="28" fill="var(--hatch)"/>

      <text x="250" y="62" text-anchor="middle" font-size="22">
        <tspan class="person-first">KHALID YOUSEF </tspan><tspan class="person-last">RUMAITHI</tspan>
      </text>
      <text class="person-role" x="250" y="80" text-anchor="middle" font-size="10.5">SENIOR EXECUTIVE OFFICER</text>
      <text class="person-name-ar" x="250" y="103" text-anchor="middle" font-size="14" direction="rtl" lang="ar">خالد يوسف الرميثي</text>
      <text class="person-role-ar" x="250" y="120" text-anchor="middle" font-size="10.5" direction="rtl" lang="ar">المدير التنفيدي</text>
      <g class="dot-row" fill="var(--brand-blue)">
        <circle cx="239" cy="135" r="3.5"/><circle cx="250" cy="135" r="3.5"/><circle cx="261" cy="135" r="3.5"/>
      </g>

      <rect class="accent-bar" x="-10" y="146" width="175" height="7" rx="3.5" fill="var(--brand-blue)"/>
      <rect class="accent-bar" x="335" y="146" width="175" height="7" rx="3.5" fill="var(--brand-blue)"/>

      <g class="column-rules" stroke="var(--hairline)" stroke-width="1">
        <line x1="0" y1="160" x2="500" y2="160"/>
        <line x1="166" y1="160" x2="166" y2="222"/>
        <line x1="334" y1="160" x2="334" y2="222"/>
      </g>
      <text class="contact-line" x="83" y="188" text-anchor="middle" font-size="9.5">krumaithi@ashbournepartners.com</text>
      <text class="contact-line" x="83" y="202" text-anchor="middle" font-size="9.5">www.ashbournepartners.com</text>
      <text class="contact-line" x="250" y="195" text-anchor="middle" font-size="9.5">+9714987650</text>
      <text class="contact-line" x="417" y="188" text-anchor="middle" font-size="9.5">Palm Terrace 07, Level 3,</text>
      <text class="contact-line" x="417" y="202" text-anchor="middle" font-size="9.5">Office 215/12, HLMZ</text>

      <rect class="icon-band" x="0" y="226" width="500" height="30" fill="var(--brand-grey)"/>
      <line x1="0" y1="241" x2="500" y2="241" stroke="var(--card-white)" stroke-width="2.5"/>
      <rect class="footer-band" x="0" y="256" width="500" height="34" fill="var(--brand-blue)"/>

      <g class="icon icon-globe" transform="translate(83 241)">
        <circle r="17" fill="var(--brand-grey)" stroke="var(--card-white)" stroke-width="2.5"/>
        <circle r="11" fill="var(--card-white)"/>
        <g fill="none" stroke="var(--brand-grey)" stroke-width="1">
          <circle r="6"/><ellipse rx="2.6" ry="6"/>
          <line x1="-6" y1="0" x2="6" y2="0"/>
        </g>
      </g>
      <g class="icon icon-phone" transform="translate(250 241)">
        <circle r="17" fill="var(--brand-grey)" stroke="var(--card-white)" stroke-width="2.5"/>
        <circle r="11" fill="var(--card-white)"/>
        <path d="M-5 -5 q2 -2 3.5 0 l1 2 q0.5 1 -0.5 2 l-1 1 q1.5 3 4 4 l1 -1 q1 -1 2 -0.5 l2 1 q2 1.5 0 3.5 q-2 2 -5 1 q-6 -3 -8 -9 q-1 -3 1 -5z" fill="var(--brand-grey)"/>
      </g>
      <g class="icon icon-pin" transform="translate(417 241)">
        <circle r="17" fill="var(--brand-grey)" stroke="var(--card-white)" stroke-width="2.5"/>
        <circle r="11" fill="var(--card-white)"/>
        <path d="M0 7 C-4 2 -5 -1 -5 -2.5 A5 5 0 0 1 5 -2.5 C5 -1 4 2 0 7z" fill="var(--brand-grey)"/>
        <circle cy="-2.5" r="1.8" fill="var(--card-white)"/>
      </g>
    </g>
  </svg>

</body>
</html>
```